VORLEX/M&P - brochure vol III

We have 2 property companies;
VORLEX – Development Consultants - http://vorlex.co.uk/
Marsh & Pennard Commercial – Commercial Property Agents - http://marshandpennard.com/
We have 2 VORLEX brochures and 1 Marsh & Pennard brochure, with almost the same content.
We need someone to design a 3rd brochure. The content will be a combination of the content of in our previous brochures. We can provide all images and text. Once the brochure is designed, we will need 2 versions – almost identical content but 2 different front covers (one for each company).
We have many reference examples of brochure designs that we love.
Any questions please let me know!
Thank you,
Greta

```html
<!DOCTYPE html>
<html lang="en">
<head>
<meta charset="utf-8">
<title>VORLEX brochure – spreads</title>
<link href="https://fonts.googleapis.com/css2?family=Lato:wght@400;700&display=swap" rel="stylesheet">
<style>
:root{
  --gold:#f9b21d;
  --charcoal:#333333;
  --ink:#111111;
  --white:#ffffff;
  --stage:#e4e1dc;
  --map-light:#e2e2e2;
  --map-mid:#d0d0d0;
  --map-dark:#5a5a5b;
}
*{box-sizing:border-box;margin:0;padding:0}
html,body{width:1200px;height:1200px;overflow:hidden}
body{background:var(--stage);font-family:'Lato',sans-serif;position:relative;color:var(--white)}
.panel-label{position:absolute;font-size:45px;font-weight:400;color:var(--charcoal);letter-spacing:1px;transform:translateX(-50%);line-height:1}
.panel{position:absolute;width:508px;height:358px;overflow:hidden;box-shadow:0 4px 14px rgba(0,0,0,.25)}
.front{left:44px;top:158px;background:var(--ink)}
.inside-one{left:658px;top:158px;background:var(--white)}
.inside-two{left:44px;top:778px;background:var(--charcoal)}
.back{left:658px;top:778px;background:var(--charcoal)}

/* front cover */
.front .masthead{position:absolute;left:0;top:0;width:100%;height:96px;background:#141414;text-align:center}
.front .brand{position:absolute;left:0;right:0;top:16px;font-size:35px;font-weight:700;color:var(--gold);letter-spacing:1px;line-height:1}
.front .rule{position:absolute;left:198px;width:112px;top:55px;height:1px;background:var(--gold)}
.front .tagline{position:absolute;left:0;right:0;top:60px;font-size:9.5px;color:var(--gold);line-height:12px;letter-spacing:.3px}
.front .hero{position:absolute;left:0;top:96px;width:100%;height:218px;background:linear-gradient(180deg,#3c3c3c 0%,#2e2e2e 45%,#222 80%,#1a1a1a 100%)}
.front .web-band{position:absolute;left:0;top:314px;width:100%;height:24px;background:var(--gold);color:var(--ink);font-size:10px;font-weight:700;letter-spacing:6px;text-align:center;line-height:24px}

/* inside one */
.inside-one .intro{position:absolute;top:10px;font-size:8.2px;color:var(--ink);line-height:10.5px;z-index:1}
.inside-one .intro.lead{left:19px;width:196px;font-weight:700}
.inside-one .intro.detail{left:224px;width:265px;text-align:justify}
.inside-one .intro.detail p+p{margin-top:10px}
.inside-one .map{position:absolute;left:0;top:70px;width:100%;height:288px;
  background:
    radial-gradient(ellipse 70% 30% at 70% 46%,rgba(249,178,29,.35),rgba(249,178,29,0) 70%),
    linear-gradient(176deg,var(--white) 0%,var(--map-light) 12%,var(--map-mid) 38%,#a9a9a9 47%,#6b6b6c 56%,var(--map-dark) 100%)}

/* inside two */
.inside-two .title{position:absolute;left:11px;top:18px;font-size:12.5px;font-weight:400;line-height:15px}
.inside-two .kicker{position:absolute;left:11px;top:53px;font-size:8.5px;color:var(--gold);font-weight:400}
.inside-two .divider{position:absolute;left:11px;top:68px;width:230px;height:1px;background:#555}
.inside-two .summary{position:absolute;left:10px;top:89px;width:113px;font-size:7.6px;line-height:10.2px;text-align:justify}
.inside-two .facts{position:absolute;left:10px;top:168px;width:122px;font-size:6.4px;line-height:9.8px}
.inside-two .facts b{color:var(--gold);font-size:7.6px;font-weight:400}
.inside-two .photo{position:absolute;background:linear-gradient(160deg,#c9d3dc,#7d8894 60%,#4a4f55)}
.inside-two .photo.tower{left:132px;top:92px;width:114px;height:174px}
.inside-two .photo.street{left:10px;top:274px;width:113px;height:64px;background:linear-gradient(160deg,#e5e9ee,#a0614a 55%,#4e4a48)}
.inside-two .photo.entrance{left:132px;top:274px;width:114px;height:64px;background:linear-gradient(160deg,#d7d7d7,#8b4a3a 55%,#3f3a38)}
.inside-two .photo.hero{left:254px;top:0;width:254px;height:358px;background:linear-gradient(170deg,#f2f0e6 0%,#b7633f 40%,#c99a4a 70%,#7a6a55 100%)}

/* back */
.back .team{position:absolute;top:43px;width:122px;text-align:center}
.back .team.one{left:46px}.back .team.two{left:193px}.back .team.three{left:339px}
.back .portrait{height:92px;background:linear-gradient(180deg,#d8d8d8,#7c7c7c 60%,#3a3a3a)}
.back .card{height:50px;background:var(--gold);color:var(--charcoal);padding-top:4px}
.back .name{font-size:8.5px;line-height:10px}
.back .role{font-size:6.5px;line-height:9px}
.back .email{font-size:8px;font-weight:700;margin-top:5px;color:var(--ink)}
.back .contact{position:absolute;left:0;right:0;text-align:center;font-size:10px;line-height:12px}
.back .icon{position:absolute;left:247px;width:14px;height:14px}
</style>
</head>
<body>

<div class="panel-label" style="left:288px;top:90px">FRONT</div>
<div class="panel-label" style="left:950px;top:90px">INSIDE 1</div>
<div class="panel-label" style="left:334px;top:708px">INSIDE 2</div>
<div class="panel-label" style="left:916px;top:708px">BACK</div>

<section class="panel front">
  <div class="masthead">
    <div class="brand">VORLEX</div>
    <div class="rule"></div>
    <div class="tagline">LONDON'S DEVELOPMENT<br>CONSULTANT</div>
  </div>
  <div class="hero" role="img" aria-label="Darkened photograph of an office building frontage and pedestrian crossing"></div>
  <div class="web-band">WWW.VORLEX.CO.UK</div>
</section>

<section class="panel inside-one">
  <div class="map" role="img" aria-label="Map of London boroughs with South and East London shaded dark grey and the River Thames traced in gold"></div>
  <div class="intro lead">VORLEX Property is a leading London based development consultancy specialising in the acquisition and disposal of brownfield sites with potential for residential development.</div>
  <div class="intro detail">
    <p>Our expertise is in identifying opportunities where developers can add value through planning permission or strategic asset management. Our considerable knowledge of the development market and creative.</p>
    <p>Approach to delivering maximum value, has enabled us to become one of the most active development consultancies in South/East London and Kent.</p>
  </div>
</section>

<section class="panel inside-two">
  <div class="title">42 HARLOW STREET,<br>LONDON SE1</div>
  <div class="kicker">LANDMARK DEVELOPMENT</div>
  <div class="divider"></div>
  <div class="summary">Acquisition of an existing office building with the benefit of full planning permission for the development of a 16 storey mixed use scheme.</div>
  <div class="facts">
    <b>Scheme</b> – 9 x Luxury apartments;<br>16 storeys<br>
    <b>Borough</b> – Southwark<br>
    <b>Existing use</b> – Office<br>
    <b>Vendor/Selling agent</b> – Kelburn<br>Real Estate<br>
    <b>Purchaser</b> – Private Client<br>
    <b>Project value</b> – £20,000,000
  </div>
  <div class="photo tower" role="img" aria-label="Photograph of the proposed glass tower beside office blocks"></div>
  <div class="photo street" role="img" aria-label="Photograph of the brick building on the street corner"></div>
  <div class="photo entrance" role="img" aria-label="Photograph of the building entrance"></div>
  <div class="photo hero" role="img" aria-label="Photograph of the brick office building in autumn sunlight"></div>
</section>

<section class="panel back">
  <div class="team one">
    <div class="portrait" role="img" aria-label="Portrait of Daniel Reyes"></div>
    <div class="card"><div class="name">DANIEL REYES</div><div class="role">MANAGING DIRECTOR</div><div class="email">daniel@vorlex.co.uk</div></div>
  </div>
  <div class="team two">
    <div class="portrait" role="img" aria-label="Portrait of Oliver Brand"></div>
    <div class="card"><div class="name">OLIVER BRAND</div><div class="role">LAND CONSULTANT</div><div class="email">oliver@vorlex.co.uk</div></div>
  </div>
  <div class="team three">
    <div class="portrait" role="img" aria-label="Portrait of Greta Ashdown"></div>
    <div class="card"><div class="name">GRETA ASHDOWN</div><div class="role">OFFICE MANAGER</div><div class="email">greta@vorlex.co.uk</div></div>
  </div>

  <svg class="icon" style="top:212px" viewBox="0 0 14 14"><path d="M3 2h3l1 3-2 1c1 2 2 3 4 4l1-2 3 1v3c-6 0-10-4-10-10z" fill="var(--gold)"/></svg>
  <div class="contact" style="top:226px">0207 555 0182</div>
  <svg class="icon" style="top:242px" viewBox="0 0 14 14"><circle cx="7" cy="7" r="5.5" fill="none" stroke="var(--gold)" stroke-width="1.6"/><path d="M1.5 7h11M7 1.5c-3 3-3 8 0 11M7 1.5c3 3 3 8 0 11" fill="none" stroke="var(--gold)" stroke-width="1.2"/></svg>
  <div class="contact" style="top:256px">WWW.VORLEX.CO.UK</div>
  <svg class="icon" style="top:270px" viewBox="0 0 14 14"><rect x="1" y="3" width="12" height="8" fill="var(--gold)"/><path d="M1 3l6 5 6-5" fill="none" stroke="var(--charcoal)" stroke-width="1"/></svg>
  <div class="contact" style="top:284px">INFO@VORLEX.CO.UK</div>
  <svg class="icon" style="top:300px" viewBox="0 0 14 14"><path d="M7 1a4 4 0 0 1 4 4c0 3-4 8-4 8S3 8 3 5a4 4 0 0 1 4-4z" fill="var(--gold)"/><circle cx="7" cy="5" r="1.5" fill="var(--charcoal)"/></svg>
  <div class="contact" style="top:314px">58 CALDER ROW&nbsp;&nbsp;LONDON SE1 4XQ</div>
</section>

</body>
</html>
```